Brindle 48 Focus Wheel

We need a professional **framework wheel diagram** designed for our detection dog training manual.

Our business is **Brindle 48 Dog Training**, and this graphic represents our **Detection Training Model**.

Please use the **attached reference images** as a guide for the structure and layout of the wheel.

### What we need

1. **Full wheel graphic**

* Clean circular framework wheel
* Similar structure to the attached example
* Clear sections and text
* Professional training manual style
* Transparent background

2. **Individual segment pieces**

We also need the **inner sections broken into separate pieces** (like the second reference image).

This will allow us to place each section on different pages of the manual when explaining the concepts.

Each piece should look like a **slice of the wheel**.

### Style

The design should look:

• Professional
• Clean and modern
• Structured and easy to read
• Suitable for a training manual

Avoid cartoon styles or clipart.

### Colours

Please use our brand colour palette (see attached image):

* Dark navy blue
* Steel blue
* Light blue
* White
* Light grey
* Dark grey

### Files required

Final files must include:

* Vector files (AI or EPS)
* Transparent PNG
* High-resolution PDF

Please also provide **each segment exported individually**

```html
<!DOCTYPE html>
<html lang="en">
<head>
<meta charset="utf-8">
<title>Brindle 48 Focus Wheel</title>
<link href="https://fonts.googleapis.com/css2?family=Montserrat:wght@400;500;600;700&display=swap" rel="stylesheet">
<style>
  :root {
    --navy: #304b69;
    --steel: #66a3ba;
    --grey-dark: #666666;
    --grey-light: #f5f5f5;
    --white: #ffffff;
  }
  html, body {
    margin: 0;
    padding: 0;
    width: 1173px;
    height: 1200px;
    overflow: hidden;
    background: var(--white);
  }
  .focus-wheel {
    display: block;
    width: 1173px;
    height: 1200px;
    font-family: "Montserrat", sans-serif;
  }
  .outer-ring { fill: none; stroke: var(--grey-dark); stroke-width: 80; }
  .area-segment { fill: var(--navy); stroke: var(--white); stroke-width: 4; }
  .dog-band { fill: var(--grey-light); stroke: var(--white); stroke-width: 4; }
  .handler-band { fill: var(--steel); }
  .dog-segment { fill: var(--steel); stroke: var(--white); stroke-width: 4; }
  .handler-segment { fill: var(--grey-dark); stroke: var(--white); stroke-width: 4; }
  .core { fill: var(--navy); stroke: var(--white); stroke-width: 6; }
  .core-badge { fill: var(--white); }
  .ring-title { fill: var(--white); font-weight: 600; font-size: 84px; letter-spacing: 4px; }
  .band-title { font-weight: 600; font-size: 42px; letter-spacing: 3px; }
  .band-title--dog { fill: var(--navy); }
  .band-title--handler { fill: var(--white); }
  .core-title { fill: var(--white); font-weight: 600; font-size: 27px; letter-spacing: 2px; }
  .area-label { fill: var(--white); font-weight: 600; font-size: 40px; text-anchor: middle; dominant-baseline: middle; }
  .foundation-label { fill: var(--white); font-weight: 400; font-size: 30px; text-anchor: middle; dominant-baseline: middle; }
  .core-name { fill: var(--navy); font-weight: 700; font-size: 30px; text-anchor: middle; dominant-baseline: middle; }
</style>
</head>
<body>
<svg class="focus-wheel" viewBox="0 0 1890 1934" xmlns="http://www.w3.org/2000/svg" role="img" aria-label="Brindle 48 Focus Wheel: detection training model">
  <defs>
    <path id="arc-area-top" d="M 210 972 A 742 742 0 0 1 1694 972"/>
    <path id="arc-area-bottom" d="M 159 972 A 793 793 0 0 0 1745 972"/>
    <path id="arc-dog-top" d="M 539 972 A 413 413 0 0 1 1365 972"/>
    <path id="arc-handler-bottom" d="M 505 972 A 447 447 0 0 0 1399 972"/>
    <path id="arc-core-top" d="M 845 972 A 107 107 0 0 1 1059 972"/>
    <path id="arc-core-bottom" d="M 826 972 A 126 126 0 0 0 1078 972"/>
  </defs>

  <!-- Operational capability ring -->
  <circle class="outer-ring" cx="952" cy="972" r="765"/>
  <text class="ring-title"><textPath href="#arc-area-top" startOffset="50%" text-anchor="middle">OPERATIONAL CAPABILITY AREA</textPath></text>
  <text class="ring-title"><textPath href="#arc-area-bottom" startOffset="50%" text-anchor="middle">OPERATIONAL CAPABILITY AREA</textPath></text>

  <!-- Operational capability areas -->
  <g class="area-segments">
    <path class="area-segment" d="M952 972 L1659 972 A707 707 0 0 0 1531.2 566.5 Z"/>
    <path class="area-segment" d="M952 972 L1531.2 566.5 A707 707 0 0 0 1193.8 307.6 Z"/>
    <path class="area-segment" d="M952 972 L1193.8 307.6 A707 707 0 0 0 710.2 307.6 Z"/>
    <path class="area-segment" d="M952 972 L710.2 307.6 A707 707 0 0 0 372.8 566.5 Z"/>
    <path class="area-segment" d="M952 972 L372.8 566.5 A707 707 0 0 0 245 972 Z"/>
    <path class="area-segment" d="M952 972 L245 972 A707 707 0 0 0 452.1 1471.9 Z"/>
    <path class="area-segment" d="M952 972 L452.1 1471.9 A707 707 0 0 0 952 1679 Z"/>
    <path class="area-segment" d="M952 972 L952 1679 A707 707 0 0 0 1451.9 1471.9 Z"/>
    <path class="area-segment" d="M952 972 L1451.9 1471.9 A707 707 0 0 0 1659 972 Z"/>
  </g>

  <!-- Foundation bands -->
  <circle class="dog-band" cx="952" cy="972" r="455"/>
  <path class="handler-band" d="M497 972 A455 455 0 0 0 1407 972 Z"/>
  <text class="band-title band-title--dog"><textPath href="#arc-dog-top" startOffset="50%" text-anchor="middle">DOG FOUNDATIONS</textPath></text>
  <text class="band-title band-title--handler"><textPath href="#arc-handler-bottom" startOffset="50%" text-anchor="middle">HANDLER FOUNDATIONS</textPath></text>

  <!-- Dog foundations -->
  <g class="dog-segments">
    <path class="dog-segment" d="M952 972 L1352 972 A400 400 0 0 0 1279.7 742.6 Z"/>
    <path class="dog-segment" d="M952 972 L1279.7 742.6 A400 400 0 0 0 1088.8 596.1 Z"/>
    <path class="dog-segment" d="M952 972 L1088.8 596.1 A400 400 0 0 0 815.2 596.1 Z"/>
    <path class="dog-segment" d="M952 972 L815.2 596.1 A400 400 0 0 0 624.3 742.6 Z"/>
    <path class="dog-segment" d="M952 972 L624.3 742.6 A400 400 0 0 0 552 972 Z"/>
  </g>

  <!-- Handler foundations -->
  <g class="handler-segments">
    <path class="handler-segment" d="M952 972 L552 972 A400 400 0 0 0 669.2 1254.8 Z"/>
    <path class="handler-segment" d="M952 972 L669.2 1254.8 A400 400 0 0 0 952 1372 Z"/>
    <path class="handler-segment" d="M952 972 L952 1372 A400 400 0 0 0 1234.8 1254.8 Z"/>
    <path class="handler-segment" d="M952 972 L1234.8 1254.8 A400 400 0 0 0 1352 972 Z"/>
  </g>

  <!-- Core -->
  <circle class="core" cx="952" cy="972" r="135"/>
  <circle class="core-badge" cx="952" cy="972" r="88"/>
  <text class="core-name" x="952" y="974">Brindle 48</text>
  <text class="core-title"><textPath href="#arc-core-top" startOffset="50%" text-anchor="middle">DETECTION</textPath></text>
  <text class="core-title"><textPath href="#arc-core-bottom" startOffset="50%" text-anchor="middle">CAPABILITIES</textPath></text>

  <!-- Area labels -->
  <g class="area-labels">
    <text class="area-label" x="946" y="410">Distractions</text>
    <text class="area-label" x="592" y="525">Development</text>
    <text class="area-label" x="1310" y="525">Behaviour</text>
    <text class="area-label" x="388" y="815">Integrity</text>
    <text class="area-label" x="1517" y="815">Handler</text>
    <text class="area-label" x="405" y="1143">Target</text>
    <text class="area-label" x="405" y="1193">Odour</text>
    <text class="area-label" x="1495" y="1143">Search</text>
    <text class="area-label" x="1495" y="1193">Method</text>
    <text class="area-label" x="715" y="1498">Deployment</text>
    <text class="area-label" x="1165" y="1498">Reinforcement</text>
  </g>

  <!-- Foundation labels -->
  <g class="foundation-labels">
    <text class="foundation-label" x="952" y="647">Health &amp;</text>
    <text class="foundation-label" x="952" y="681">Physical</text>
    <text class="foundation-label" x="952" y="716">Wellbeing</text>
    <text class="foundation-label" x="775" y="731">Genetic</text>
    <text class="foundation-label" x="775" y="766">Suitability</text>
    <text class="foundation-label" x="1133" y="731">Reward</text>
    <text class="foundation-label" x="1133" y="766">Value</text>
    <text class="foundation-label" x="677" y="882">Arousal</text>
    <text class="foundation-label" x="677" y="917">Regulation</text>
    <text class="foundation-label" x="1215" y="890">Engagement</text>
    <text class="foundation-label" x="1215" y="925">Relationship</text>
    <text class="foundation-label" x="695" y="1060">Dog Safety</text>
    <text class="foundation-label" x="1192" y="1060">Read the Dog</text>
    <text class="foundation-label" x="843" y="1194">Search</text>
    <text class="foundation-label" x="843" y="1229">Coverage</text>
    <text class="foundation-label" x="1070" y="1186">Minimal</text>
    <text class="foundation-label" x="1070" y="1221">Necessary</text>
    <text class="foundation-label" x="1070" y="1255">Involvement</text>
  </g>
</svg>
</body>
</html>
```